Video production company website

VistaKeel Productions is a video and photography production company serving many Fortune 500 clients traveling to Hawaii and International Destinations. Our primary focus is the Corporate and Incentive group market, and offer both photography and video services. In addition, we also create custom marketing, sales, art, and real estate productions.

Target Market(s)

Corporate Incentive Travel Groups

Industry/Entity Type

Videography

Number of Pages Required

4 page

Requirements
Must have
• see doc with content. This will ultimately be needed to be a wordpress design so we can update ourselves.
Nice to have
• sleek design, professional, cutting edge, modern
Should not have
• too much Hawaii Feel, some ok but we do travel international

```html
<!DOCTYPE html>
<html lang="en">
<head>
<meta charset="utf-8">
<title>VistaKeel Productions</title>
<link href="https://fonts.googleapis.com/css2?family=Open+Sans:ital,wght@0,300;0,400;0,600;0,700;1,400&family=Cormorant+Garamond:ital,wght@1,500&display=swap" rel="stylesheet">
<style>
:root{
  --ink:#333;
  --muted:#777;
  --light:#f2f2f2;
  --line:#d9d9d9;
  --white:#fff;
  --bar:#5b9bd5;
  --bar-bg:#dde3ea;
  --night:#2e2a55;
  --night2:#4a4379;
  --platinum:#f0595b;
  --gold:#37a6de;
  --silver:#f9c13a;
  --special:#1cc2bf;
  --price:#e8665f;
  --footer:#0c0c0c;
  --social:#3d6fb0;
}
*{box-sizing:border-box;margin:0;padding:0}
html,body{width:1200px;height:4737px;overflow:hidden}
body{position:relative;font-family:"Open Sans",Arial,sans-serif;color:var(--ink);background:var(--white)}
section,header,footer{position:absolute;left:0;width:1200px}
.abs{position:absolute}
.section-title{position:absolute;left:0;width:1200px;text-align:center;font-size:30px;font-weight:400;color:var(--ink)}
.section-title::after{content:"";display:block;width:110px;height:2px;background:#555;margin:10px auto 0}
.intro{position:absolute;left:300px;width:600px;text-align:center;font-size:14px;line-height:24px;color:var(--muted)}
.btn{position:absolute;display:flex;align-items:center;justify-content:center;background:var(--white);color:var(--ink);font-size:15px;border-radius:4px;border:1px solid #bbb}

/* hero */
.hero{top:0;height:568px;background:linear-gradient(180deg,#3a4450 0%,#4f5a52 35%,#3b4a2e 70%,#1f2a1a 100%)}
.nav{position:absolute;top:46px;font-size:13px;color:var(--white);text-transform:uppercase}
.logo-ring{position:absolute;left:566px;top:14px;width:68px;height:68px;border:2px solid var(--white);border-radius:50%}
.logo-name{position:absolute;left:520px;top:86px;width:160px;text-align:center;color:var(--white);font-size:9px;letter-spacing:1px}
.hero-script{position:absolute;left:0;top:210px;width:1200px;text-align:center;font-family:"Cormorant Garamond",Georgia,serif;font-style:italic;font-size:38px;color:var(--white)}
.hero-rule{position:absolute;left:372px;width:456px;height:3px;background:var(--white)}
.hero-title{position:absolute;top:284px;width:1200px;text-align:center;font-size:28px;color:var(--white);letter-spacing:1px}
.hero-sub{position:absolute;top:324px;width:1200px;text-align:center;font-size:15px;line-height:20px;color:#eee}
.hero-arrow{position:absolute;top:264px;width:38px;height:38px;background:rgba(255,255,255,.35);border-radius:4px}

/* specialties */
.tile{position:absolute;top:714px;width:307px;height:208px}
.tile-label{position:absolute;left:0;bottom:20px;width:100%;height:46px;background:rgba(0,0,0,.55);color:var(--white);display:flex;align-items:center;justify-content:center;font-size:16px}

/* about */
.about{top:963px;height:515px;background:var(--light)}
.skill{position:absolute;left:641px;width:376px;font-size:13px;color:var(--ink)}
.skill-track{height:12px;background:var(--bar-bg);margin-top:6px}
.skill-fill{height:12px;background:var(--bar)}

/* timeline */
.timeline{top:1478px;height:897px;background:radial-gradient(ellipse at 30% 40%,var(--night2),var(--night) 70%)}
.post{position:absolute;background:var(--white);padding:24px 24px 0;box-shadow:0 4px 16px rgba(0,0,0,.4)}
.post h3{font-size:24px;font-weight:400;margin-top:10px}
.post .meta{font-size:10px;color:var(--muted)}
.post p{font-size:11px;line-height:16px;color:var(--muted);margin-top:14px}
.post .more{font-size:11px;color:var(--ink);margin-top:6px}

/* packages */
.package{position:absolute;top:2526px;width:231px;height:379px;background:var(--white);box-shadow:0 2px 10px rgba(0,0,0,.15);text-align:center}
.package-head{height:160px;color:var(--white);font-size:28px;font-weight:600;padding-top:30px;line-height:36px;clip-path:polygon(0 0,100% 0,100% 80%,50% 100%,0 80%)}
.package p{font-size:13px;line-height:20px;color:var(--muted);margin:22px 24px 0}
.package .price{font-size:36px;font-weight:300;color:var(--price);margin-top:4px}
.package .price small{font-size:18px}
.package .buy{width:150px;height:42px;margin:18px auto 0;border-radius:4px;color:var(--white);font-size:14px;font-weight:600;display:flex;align-items:center;justify-content:center}

/* best band */
.band{top:2937px;height:167px;background:linear-gradient(180deg,#1b1f27,#3a3f48 50%,#15181e);display:flex;align-items:center;justify-content:center;font-size:58px;font-weight:300;color:var(--white)}

/* gallery */
.shot{position:absolute}
.dot{position:absolute;top:3652px;width:12px;height:12px;background:#bbb}

/* contact */
.contact-info{position:absolute;left:110px;top:3825px;font-size:15px;line-height:26px;color:var(--ink)}
.social{position:absolute;top:4100px;width:46px;height:46px;border-radius:50%;background:var(--social)}

/* newsletter */
.newsletter{top:4188px;height:505px;background:linear-gradient(180deg,#8fa3b4 0%,#6d8aa4 40%,#3f7290 75%,#2c5a74 100%)}
.field-label{position:absolute;left:118px;font-size:14px;color:var(--white)}
.field{position:absolute;left:240px;width:430px;height:36px;background:rgba(255,255,255,.85)}
.login{position:absolute;left:701px;top:28px;width:389px;height:426px;background:rgba(40,40,40,.7);padding:22px 24px;color:var(--white)}
.login .box{height:34px;background:rgba(255,255,255,.85);margin-top:14px;font-size:12px;color:#999;padding:9px 12px}
.footer{top:4693px;height:44px;background:var(--footer);color:var(--white);font-size:13px;display:flex;align-items:center;justify-content:center}
</style>
</head>
<body>

<header class="hero" role="img" aria-label="Sunset over green hillside with tropical valley">
  <span class="nav" style="left:226px">Home</span>
  <span class="nav" style="left:306px">About Us ▾</span>
  <span class="nav" style="left:428px">Contact ▾</span>
  <div class="logo-ring"></div>
  <div class="logo-name">VISTAKEEL PRODUCTIONS</div>
  <span class="nav" style="left:680px">Gallery ▾</span>
  <span class="nav" style="left:792px">Pages</span>
  <span class="nav" style="left:874px">Client</span>
  <div class="hero-rule" style="top:208px"></div>
  <div class="hero-script">Lorem ipsum dolor sit amet</div>
  <div class="hero-rule" style="top:262px"></div>
  <div class="hero-title">MAECENAS DIAM ANTE</div>
  <div class="hero-sub">Lorem ipsum dolor sit amet, consectetur<br>adipiscing elit.</div>
  <div class="btn" style="left:527px;top:384px;width:146px;height:40px;background:transparent;color:var(--white);border-color:var(--white)">View</div>
  <div class="hero-arrow" style="left:114px"><svg width="38" height="38"><path d="M22 12 L15 19 L22 26" stroke="#fff" stroke-width="3" fill="none"/></svg></div>
  <div class="hero-arrow" style="left:1048px"><svg width="38" height="38"><path d="M16 12 L23 19 L16 26" stroke="#fff" stroke-width="3" fill="none"/></svg></div>
</header>

<section class="specialties" style="top:568px;height:395px">
  <h2 class="section-title" style="top:22px">My Specialties</h2>
  <p class="intro" style="top:92px">Pellentesque pellentesque volutpat leo, at pretium arcu rutrum non. Aenean sit amet posuere urna. In volutpat sit amet magna sed vulputate.</p>
</section>
<div class="tile" style="left:110px;background:linear-gradient(160deg,#5a2f8a,#c23c7a 50%,#2a1a40)" role="img" aria-label="Evening event with lit palm trees"><div class="tile-label">LOREM IPSUM</div></div>
<div class="tile" style="left:445px;background:linear-gradient(160deg,#3f6b2d,#8db45a 50%,#4a6a3a)" role="img" aria-label="Group of guests outdoors"><div class="tile-label">LOREM IPSUM</div></div>
<div class="tile" style="left:780px;background:linear-gradient(180deg,#f3b54a,#e0782b 55%,#2a2018)" role="img" aria-label="Sunset behind palm trees"><div class="tile-label">LOREM IPSUM</div></div>

<section class="about">
  <div class="abs" style="left:0;top:0;width:600px;height:515px;background:linear-gradient(180deg,#e9a64a,#c77a3f 40%,#4e6a3a 80%,#2f3f22)" role="img" aria-label="Producer standing on coast at sunset"></div>
  <h2 class="section-title" style="left:600px;width:300px;top:14px;font-size:28px">About Us</h2>
  <div class="abs" style="left:641px;top:84px;width:420px;font-size:12px;line-height:17px;color:var(--muted)">
    <div>Marcus Delane</div>
    <div style="color:var(--ink);font-weight:600">Owner and Producer</div>
    <div style="margin-top:6px">Before years of experience producing photography and video for corporate incentive and convention groups, Marcus worked for travel productions as a production assistant and cameraman for a weekly show.</div>
    <div style="margin-top:10px;color:var(--ink)">Read more →</div>
  </div>
  <div class="skill" style="top:278px">Photo Editing <span style="color:var(--bar)">80%</span><div class="skill-track"><div class="skill-fill" style="width:78%"></div></div></div>
  <div class="skill" style="top:335px">Video Editing <span style="color:var(--bar)">60%</span><div class="skill-track"><div class="skill-fill" style="width:58%"></div></div></div>
  <div class="skill" style="top:392px">Studio Photography <span style="color:var(--bar)">65%</span><div class="skill-track"><div class="skill-fill" style="width:62%"></div></div></div>
  <div class="skill" style="top:449px">Video <span style="color:var(--bar)">70%</span><div class="skill-track"><div class="skill-fill" style="width:44%"></div></div></div>
</section>

<section class="timeline">
  <h2 class="section-title" style="top:28px;color:var(--white)">Timeline</h2>
  <div class="abs" style="left:593px;top:96px;width:2px;height:680px;background:rgba(255,255,255,.5)"></div>
  <div class="abs" style="left:587px;top:168px;width:14px;height:14px;border-radius:50%;background:var(--white)"></div>
  <div class="abs" style="left:587px;top:282px;width:14px;height:14px;border-radius:50%;background:var(--white)"></div>
  <article class="post" style="left:123px;top:164px;width:442px;height:480px">
    <div style="height:256px;background:linear-gradient(160deg,#6a3a9a,#d04b8c 50%,#2b1a44)" role="img" aria-label="Nighttime party under lit palms"></div>
    <h3>Maecenas diam</h3>
    <div class="meta">Lena Ortiz · Wednesday, March 04, 2015</div>
    <p>Lorem ipsum dolor sit amet, consectetur adipiscing elit. Curabitur sit amet urna vel turpis gravida suscipit ac sed metus. Donec id nunc sed ipsum dapibus lobortis sit amet non turpis. Aenean luctus dignissim magna ac egestas. Pellentesque sit amet arcu lectus, interdum lorem id, ultrices neque.</p>
    <div class="more">Read more →</div>
  </article>
  <article class="post" style="left:632px;top:278px;width:432px;height:480px">
    <div style="height:256px;background:#111;display:flex;flex-direction:column;align-items:center;justify-content:center;gap:14px">
      <div style="width:120px;height:120px;border-radius:50%;background:#2a2a2a"></div>
      <div style="color:var(--white);font-size:20px;letter-spacing:1px">VISTAKEEL PRODUCTIONS</div>
    </div>
    <h3>Maecenas diam</h3>
    <div class="meta">Lena Ortiz · Wednesday, March 04, 2015</div>
    <p>Lorem ipsum dolor sit amet, consectetur adipiscing elit. Curabitur sit amet urna vel turpis gravida suscipit ac sed metus. Donec id nunc sed ipsum dapibus lobortis sit amet non turpis. Aenean luctus dignissim magna ac egestas. Pellentesque sit amet arcu lectus, interdum lorem id, ultrices neque.</p>
    <div class="more">Read more →</div>
  </article>
  <div class="btn" style="left:932px;top:818px;width:135px;height:38px;font-size:13px">Older Posts</div>
</section>

<section class="packages" style="top:2375px;height:562px">
  <h2 class="section-title" style="top:30px">Photo Packages</h2>
  <p class="intro" style="top:94px">Pellentesque pellentesque volutpat leo, at pretium arcu rutrum non. Aenean sit amet posuere urna. In volutpat sit amet magna sed vulputate.</p>
</section>
<div class="package" style="left:110px"><div class="package-head" style="background:var(--platinum)">Platinum</div><p>Maecenas tempor sollicitudin magna. Mauris consequat congue suscipit.</p><div class="price"><small>$</small>2500</div><div class="buy" style="background:var(--platinum)">View</div></div>
<div class="package" style="left:360px"><div class="package-head" style="background:var(--gold)">Gold</div><p>Maecenas tempor sollicitudin magna. Mauris consequat congue suscipit.</p><div class="price"><small>$</small>1500</div><div class="buy" style="background:var(--gold)">View</div></div>
<div class="package" style="left:609px"><div class="package-head" style="background:var(--silver)">Silver</div><p>Maecenas tempor sollicitudin magna. Mauris consequat congue suscipit.</p><div class="price"><small>$</small>2000</div><div class="buy" style="background:var(--silver)">View</div></div>
<div class="package" style="left:859px"><div class="package-head" style="background:var(--special)">VistaKeel<br>Special</div><p>Maecenas tempor sollicitudin magna. Mauris consequat congue suscipit.</p><div class="price"><small>$</small>3000</div><div class="buy" style="background:var(--special)">View</div></div>

<section class="band" role="img" aria-label="Dark ocean surface">The Best of the Best</section>

<section class="gallery" style="top:3104px;height:591px">
  <h2 class="section-title" style="top:28px">Gallery</h2>
  <p class="intro" style="top:92px">Pellentesque pellentesque volutpat leo, at pretium arcu rutrum non. Aenean sit amet posuere urna. In volutpat sit amet magna sed vulputate.</p>
</section>
<div class="shot" style="left:0;top:3325px;width:95px;height:183px;background:linear-gradient(180deg,#6c8fb3,#3b5a7a)" role="img" aria-label="Waterfront scene"></div>
<div class="shot" style="left:107px;top:3325px;width:272px;height:183px;background:linear-gradient(160deg,#e0d8d0,#b22a2a 50%,#6a6a70)" role="img" aria-label="Red vintage car"></div>
<div class="shot" style="left:388px;top:3268px;width:411px;height:269px;background:linear-gradient(180deg,#3a4a8a,#9a86b8 45%,#e7b08a 60%,#1a1a2a)" role="img" aria-label="Palm silhouettes at dusk over pool"></div>
<div class="shot" style="left:808px;top:3325px;width:272px;height:183px;background:linear-gradient(180deg,#2b3a6a,#3f6a3a 60%,#1f3020)" role="img" aria-label="Evening lawn event video"><svg class="abs" style="left:116px;top:72px" width="40" height="40"><path d="M6 2 L36 20 L6 38 Z" fill="#fff"/></svg></div>
<div class="shot" style="left:1093px;top:3325px;width:107px;height:183px;background:linear-gradient(160deg,#2a1a50,#6a3a9a)" role="img" aria-label="Lit trees at night"></div>
<div class="abs" style="left:0;top:3556px;width:1200px;text-align:center;font-size:13px;color:var(--muted)">Duis volutpat</div>
<div class="btn" style="left:522px;top:3590px;width:146px;height:42px;border:2px solid #999">View</div>
<div class="dot" style="left:557px;background:#333"></div>
<div class="dot" style="left:579px"></div>
<div class="dot" style="left:601px"></div>
<div class="dot" style="left:623px"></div>

<section class="contact" style="top:3695px;height:493px">
  <div class="abs" style="left:110px;top:0;width:980px;height:1px;background:var(--line)"></div>
  <h2 class="section-title" style="top:20px">Contact Us</h2>
  <p class="intro" style="top:84px;font-size:13px">Maecenas diam ante, posuere nec mi non, semper pharetra nulla.</p>
</section>
<div class="contact-info">
  <div style="font-size:18px;margin-bottom:16px">United States</div>
  <div>VistaKeel Productions, LLC</div>
  <div>P.O. Box 418-207</div>
  <div>Lanford HI 96821</div>
  <div style="margin-top:12px;font-size:13px">☎&nbsp; (555) 310-4472</div>
  <div style="font-size:13px">▤&nbsp; (555) 310-4489</div>
  <div style="font-size:18px;margin-top:58px">Keep in touch</div>
</div>
<div class="social" style="left:110px"></div>
<div class="social" style="left:168px"></div>
<div class="social" style="left:226px"></div>
<div class="social" style="left:284px"></div>
<div class="abs" style="left:420px;top:3827px;width:670px;height:329px;background:linear-gradient(135deg,#e4e1d8,#cfd8c4 55%,#a9c4de 80%)" role="img" aria-label="Street map of office location">
  <svg class="abs" style="left:290px;top:118px" width="24" height="34"><path d="M12 0 C5 0 0 5 0 12 C0 21 12 34 12 34 C12 34 24 21 24 12 C24 5 19 0 12 0Z" fill="#d9413b"/><circle cx="12" cy="12" r="4" fill="#fff"/></svg>
</div>

<section class="newsletter" role="img" aria-label="Pool overlooking the ocean">
  <h2 class="section-title" style="left:110px;width:580px;top:12px;color:var(--white);font-size:28px">Newsletter</h2>
  <span class="field-label" style="top:120px">Name :</span><div class="field" style="top:110px"></div>
  <span class="field-label" style="top:172px">Company Info :</span><div class="field" style="top:162px"></div>
  <span class="field-label" style="top:224px">Phone :</span><div class="field" style="top:214px"></div>
  <span class="field-label" style="top:276px">Email :</span><div class="field" style="top:266px"></div>
  <span class="field-label" style="top:316px">Message :</span><div class="field" style="top:310px;height:82px"></div>
  <div class="btn" style="left:240px;top:422px;width:134px;height:40px;border:none">Send</div>
  <div class="login">
    <div style="font-size:24px">Log In</div>
    <div style="height:1px;background:rgba(255,255,255,.5);margin-top:8px"></div>
    <p style="font-size:11px;line-height:16px;margin-top:14px;color:#ddd">Lorem ipsum dolor sit amet, consectetur adipiscing elit. Curabitur sit amet urna vel turpis gravida suscipit ac sed metus.</p>
    <div class="box" style="margin-top:48px">Email</div>
    <div class="box">Password</div>
    <div class="btn" style="left:122px;top:290px;width:140px;height:38px;border:none;font-size:13px">Log In</div>
    <div class="abs" style="left:24px;top:372px;font-size:11px">☑ Stay Signed In</div>
    <div class="abs" style="right:24px;top:372px;font-size:11px">Create an Account</div>
    <div class="abs" style="left:122px;top:400px;display:flex;gap:16px">
      <span style="width:14px;height:14px;border-radius:50%;background:var(--white)"></span>
      <span style="width:14px;height:14px;border-radius:50%;background:var(--white)"></span>
      <span style="width:14px;height:14px;border-radius:50%;background:var(--white)"></span>
      <span style="width:14px;height:14px;border-radius:50%;background:var(--white)"></span>
    </div>
  </div>
</section>

<footer class="footer">All Content © VistaKeel Productions 2016</footer>

</body>
</html>
```